Business card for Financial Technology company

Hello! We'd like to create business cards for 4 members of our company. Our company is a financial technology business that provides funding for businesses. We want to give it a VC (venture captal) look and feel. Clean, fresh and minimal but with a flair of artistry. I'll include some samples of cards we like. It would be great if the back of the card was artistic (see sample files 1 and 2) and the front of the card was the business info. The name of the company is Q7 Funding.

```html
<!DOCTYPE html>
<html lang="en">
<head>
<meta charset="utf-8">
<title>Q7 Funding — Business Cards</title>
<link href="https://fonts.googleapis.com/css2?family=Montserrat:wght@400;600;700&display=swap" rel="stylesheet">
<style>
  :root {
    --backdrop: #3b3430;
    --card-white: #ffffff;
    --navy: #2a3174;
    --brand: #3a2f8c;
    --stripe-green: #8cc63f;
    --stripe-teal: #1a9b8f;
    --stripe-blue: #2b6cb0;
    --stripe-purple: #6a2c91;
    --stripe-magenta: #c2188b;
    --stripe-pink: #e6217a;
    --stripe-red: #ef3b36;
    --stripe-orange: #f7941d;
    --stripe-yellow: #fcd116;
    --url-pink: #e6217a;
    --url-green: #0f8a3c;
  }
  * { box-sizing: border-box; margin: 0; padding: 0; }
  html, body {
    width: 1200px; height: 786px; overflow: hidden;
    background: var(--backdrop);
    font-family: "Montserrat", Arial, sans-serif;
  }
  .card {
    position: absolute;
    top: 245px;
    width: 520px; height: 297px;
    background: var(--card-white);
    overflow: hidden;
    box-shadow: 0 10px 24px rgba(0,0,0,0.35);
  }
  .card--front { left: 50px; }
  .card--back { left: 630px; }

  .brand {
    position: absolute;
    display: flex; align-items: center; gap: 10px;
    color: var(--brand);
    font-weight: 700;
    font-size: 24px;
    letter-spacing: 0.5px;
    white-space: nowrap;
  }
  .brand__mark {
    width: 18px; height: 18px;
    background: var(--brand);
  }
  .card--front .brand { left: 50%; top: 62px; transform: translateX(-50%); }
  .card--back .brand { left: 50%; top: 110px; transform: translateX(-50%); }

  .stripes {
    position: absolute;
    left: 0; right: 0; top: 152px;
    display: flex; flex-direction: column; gap: 2px;
  }
  .stripes span { display: block; height: 2px; }
  .stripes .s1 { background: var(--stripe-green); height: 3px; }
  .stripes .s2 { background: var(--stripe-teal); }
  .stripes .s3 { background: var(--stripe-blue); }
  .stripes .s4 { background: var(--stripe-purple); }
  .stripes .s5 { background: var(--stripe-magenta); }
  .stripes .s6 { background: var(--stripe-pink); }
  .stripes .s7 { background: var(--stripe-red); }
  .stripes .s8 { background: var(--stripe-orange); }
  .stripes .s9 { background: var(--stripe-yellow); }

  .navy-band {
    position: absolute;
    left: 0; right: 0; top: 190px; bottom: 0;
    background: var(--navy);
  }
  .contact {
    position: absolute;
    left: 0; right: 0; top: 193px;
    text-align: center;
    color: #ffffff;
    font-size: 13px;
    line-height: 19px;
    letter-spacing: 0.3px;
    list-style: none;
    padding-left: 150px;
    text-align: left;
  }

  .back-url {
    position: absolute;
    right: 70px; bottom: 62px;
    font-size: 11px;
    letter-spacing: 0.2px;
    color: var(--url-pink);
  }
  .back-url strong { color: var(--url-green); font-weight: 700; }
</style>
</head>
<body>
  <section class="card card--front" aria-label="Card front">
    <div class="brand"><span class="brand__mark"></span>Q7 Funding</div>
    <div class="stripes" aria-hidden="true">
      <span class="s1"></span><span class="s2"></span><span class="s3"></span>
      <span class="s4"></span><span class="s5"></span><span class="s6"></span>
      <span class="s7"></span><span class="s8"></span><span class="s9"></span>
    </div>
    <div class="navy-band"></div>
    <ul class="contact">
      <li>555-014-2786</li>
      <li>info@q7funding.example</li>
      <li>www.q7funding.example</li>
    </ul>
  </section>

  <section class="card card--back" aria-label="Card back">
    <div class="brand"><span class="brand__mark"></span>Q7 Funding</div>
    <p class="back-url">www.<strong>q7funding</strong>.example</p>
  </section>
</body>
</html>
```